sydney wedding photography business needs a business card design

we need a business card design for a sydney based wedding photography and videography business. our business name is :golden hour photography and video. our target clients are 24-35 yrs female. our style is candid, organic, natural, dynamic. we are a team of young photographers and videographers, and help brides to create memories that they will cherish for the rest of their lives. the logo will be provided. we want an elegant design that reflects our style, and also want to give a great impression to our clients that we are one of the best studios in sydney and our brand means quality and premium service.

Target Market(s)

bride to be, 24-35 years old, living in sydney and surrunding areas

Industry/Entity Type

Wedding Photography

Contact Information for Business Card

address: 57 marrow lane, bexton nsw 2041
mobile: 0431872056
phone: (02) 9361 2748
info@goldenhourstudio.net.au
www.goldenhourstudio.net.au
facebook:goldenhourbridals
instagram:goldenhourbridals

Font styles to use
Serif
Sans Serif

Requirements
Nice to have
• maybe add my slogan"Moments Held In Light" if the layout looks good
Should not have
• no black color, not good idea for wedding biz card

```html
<!DOCTYPE html>
<html lang="en">
<head>
<meta charset="utf-8">
<title>Golden Hour Photography – Business Card</title>
<link rel="stylesheet" href="https://fonts.googleapis.com/css2?family=Josefin+Sans:wght@400&family=Raleway:wght@400&family=Lobster&display=swap">
<style>
  :root {
    --page: #ffffff;
    --card-light: #f8f8f8;
    --card-dark: #e6e6e6;
    --gold: #d4a514;
    --gold-deep: #b8860b;
    --gold-soft: #e9d9a6;
    --ring-tone: #dcd2bf;
  }
  * { box-sizing: border-box; margin: 0; padding: 0; }
  html, body { width: 1200px; height: 999px; overflow: hidden; background: var(--page); }
  .canvas { position: relative; width: 1200px; height: 999px; }

  .card {
    position: absolute; left: 253px; width: 695px; height: 420px; overflow: hidden;
    background: radial-gradient(ellipse at 55% 90%, var(--card-light) 0%, #efefef 50%, var(--card-dark) 100%);
  }
  .card--front { top: 52px; }
  .card--back { top: 527px; }

  .ornament {
    position: absolute; border-radius: 40% 60% 45% 55%;
    background: radial-gradient(circle, var(--gold) 0%, rgba(212,165,20,0.35) 55%, rgba(212,165,20,0) 75%);
  }
  .ornament--top-left { left: 9px; top: 8px; width: 168px; height: 120px; }
  .ornament--bottom-right { left: 519px; top: 293px; width: 168px; height: 120px; }

  .ring-art {
    position: absolute; left: 397px; top: 155px; width: 298px; height: 265px;
    border-radius: 50% 40% 0 0;
    background: linear-gradient(140deg, rgba(233,217,166,0.85) 0%, rgba(220,210,191,0.7) 45%, rgba(220,210,191,0.25) 100%);
  }
  .card--back .ring-art { top: 153px; }

  .brand { position: absolute; text-align: center; color: var(--gold); font-family: "Josefin Sans", sans-serif; font-weight: 400; }
  .brand__name { display: block; font-size: 50px; line-height: 1; letter-spacing: 1px; }
  .brand__sub { display: block; font-size: 19px; letter-spacing: 7px; margin-top: 14px; }
  .card--front .brand { left: 245px; top: 40px; width: 410px; }
  .card--back .brand { left: 145px; top: 168px; width: 410px; }

  .slogan {
    position: absolute; left: 145px; top: 283px; width: 410px; text-align: center;
    font-family: "Lobster", cursive; font-size: 20px; color: var(--gold);
  }

  .contact { position: absolute; list-style: none; font-family: "Raleway", sans-serif; color: var(--gold-deep); }
  .contact li { display: flex; align-items: center; height: 22px; font-size: 17px; }
  .contact svg { width: 18px; height: 18px; margin-right: 14px; fill: var(--gold-deep); flex: none; }
  .card--front .contact { left: 29px; top: 292px; }
  .contact li.is-light { color: var(--gold); }

  .social { position: absolute; left: 38px; top: 339px; list-style: none; font-family: "Raleway", sans-serif; color: var(--gold-deep); }
  .social li { display: flex; align-items: center; height: 29px; font-size: 18px; }
  .social .marker { width: 16px; height: 16px; border-radius: 3px; background: var(--gold-deep); margin-right: 16px; }
</style>
</head>
<body>
<div class="canvas">

  <section class="card card--front">
    <div class="ornament ornament--top-left" role="img" aria-label="Gold flourish ornament"></div>
    <div class="ring-art" role="img" aria-label="Large pale gold diamond ring illustration"></div>
    <div class="ornament ornament--bottom-right" role="img" aria-label="Gold flourish ornament"></div>

    <div class="brand">
      <span class="brand__name">Golden Hour</span>
      <span class="brand__sub">PHOTOGRAPHY</span>
    </div>

    <ul class="contact">
      <li><svg viewBox="0 0 20 20"><path d="M10 2 1 10h3v8h5v-5h2v5h5v-8h3z"/></svg>57 marrow lane, bexton nsw 2041</li>
      <li><svg viewBox="0 0 20 20"><path d="M6 1h8a1 1 0 0 1 1 1v16a1 1 0 0 1-1 1H6a1 1 0 0 1-1-1V2a1 1 0 0 1 1-1zm1 2v12h6V3zm3 13a1 1 0 1 0 0 2 1 1 0 0 0 0-2z"/></svg>0431872056</li>
      <li class="is-light"><svg viewBox="0 0 20 20"><path d="M5 2 8 6 6 8c1 3 3 5 6 6l2-2 4 3-2 3C9 18 2 11 2 4z"/></svg>(02) 9361 2748</li>
      <li class="is-light"><svg viewBox="0 0 20 20"><path d="M2 5h16v11H2zm1 1 7 5 7-5z"/></svg>info@goldenhourstudio.net.au</li>
      <li><svg viewBox="0 0 20 20"><path d="M10 2a8 8 0 1 0 0 16 8 8 0 0 0 0-16zm0 2c1 1 2 3 2 6s-1 5-2 6c-1-1-2-3-2-6s1-5 2-6zM4 9h12v2H4z"/></svg>www.goldenhourstudio.net.au</li>
    </ul>
  </section>

  <section class="card card--back">
    <div class="ornament ornament--top-left" role="img" aria-label="Gold flourish ornament"></div>
    <div class="ring-art" role="img" aria-label="Large pale gold diamond ring illustration"></div>
    <div class="ornament ornament--bottom-right" role="img" aria-label="Gold flourish ornament"></div>

    <div class="brand">
      <span class="brand__name">Golden Hour</span>
      <span class="brand__sub">PHOTOGRAPHY</span>
    </div>

    <p class="slogan">Moments Held In Light</p>

    <ul class="social">
      <li><span class="marker"></span>goldenhourbridals</li>
      <li><span class="marker"></span>goldenhourbridals</li>
    </ul>
  </section>

</div>
</body>
</html>
```